CONDOMS Packaging Design Project

we are in need of the following:
1)a colorfull display box of 36 sales pack of 2 condoms with size when folded:
W=190mm,H=80mm,D=130mm
2)sales pack of 2 retangular foil condoms with sizes when folded:
Cover-W=60mm,H=62mm,D=12mm
drawer-W=59mm,H=61mm,D=11mm
The brand is VOLK,the UPC is WARM TIDE CONDOMS because it is benzocaine based to prolong the erection.
The sales pack packaging should be innovative,attractive,easy to open in the darkness,slim, thin,flat,12mm maximum as thickness for discretion,easy to be inserted into the pocket.

Our company logo,email,and other will be uploaded at final.
Only high qualified designers are welcome on this project.
Updates

Target Market(s)

15 to 35 years old men.

Industry/Entity Type

It Company

Requirements
Must have
• the sales pack of 2 condoms should be slim,thin,flat with 12mm of thickness for discretion but with hanger part to have the product visible at the reatail stores so if you can mix the 7x7 pack packaging with halvex packaging that will be great.the both packagings are in the attached files.
The design should have:
1)Map printing sales pack and display box.
2)map cutting sales pack and display box.
Nice to have
• The sales pack packaging should be innovative,attractive,easy to open in the darkness,slim and thin for discretion,easy to be inserted into the pocket,incisive colors to attract people.It will have 2 rectangular condoms foil inside.

The brand VOLK should be noted impressively like a merrovan and Castelvardo cars are for the public to penetrate the mind of the consumers as premium quality and assurance.
Should not have
• 1)avoid large size sales pack packaging.
2)avoid to exceed 12mm as thickness of the sales pack.

```html
<!DOCTYPE html>
<html lang="en">
<head>
<meta charset="utf-8">
<title>VOLK Warm Tide Condoms – Sales Pack</title>
<link rel="stylesheet" href="https://fonts.googleapis.com/css2?family=Russo+One&family=Open+Sans:ital,wght@0,400;0,700;1,700&display=swap">
<style>
  :root {
    --stage: #f1f0ee;
    --red: #d80f0f;
    --red-deep: #a30606;
    --red-bright: #ee1c1c;
    --black: #111111;
    --charcoal: #1c1c1c;
    --silver: #b9b9b9;
    --silver-light: #e8e8e8;
    --white: #ffffff;
  }
  * { margin: 0; padding: 0; box-sizing: border-box; }
  html, body { width: 1200px; height: 900px; overflow: hidden; background: var(--stage); }
  .canvas { position: relative; width: 1200px; height: 900px; }

  .hanger-tab {
    position: absolute; left: 460px; top: 80px; width: 340px; height: 180px;
    background: linear-gradient(180deg, var(--red-bright) 0%, var(--red) 55%, var(--red-deep) 100%);
    border-radius: 6px 6px 0 0;
  }
  .hang-slot {
    position: absolute; left: 110px; top: 18px; width: 120px; height: 22px;
    background: var(--stage); border-radius: 11px;
  }
  .tab-brand {
    position: absolute; left: 0; right: 0; top: 56px;
    display: flex; align-items: center; justify-content: center; gap: 12px;
  }
  .tab-brand-mark { width: 22px; height: 22px; border-radius: 50%; background: var(--black); }
  .tab-brand-name {
    font-family: "Russo One", sans-serif; font-size: 40px; color: var(--black); letter-spacing: 2px;
  }
  .tab-tagline {
    position: absolute; left: 0; right: 0; top: 126px; text-align: center;
    font-family: "Open Sans", sans-serif; font-size: 25px; color: var(--white); letter-spacing: 0.5px;
  }

  .side-panel {
    position: absolute; left: 270px; top: 260px; width: 110px; height: 560px; overflow: hidden;
    background: linear-gradient(90deg, var(--black) 0%, var(--charcoal) 60%, #2a2a2a 100%);
  }
  .side-bands { position: absolute; left: 0; top: 0; width: 110px; height: 560px; }

  .front-panel {
    position: absolute; left: 380px; top: 260px; width: 500px; height: 560px; overflow: hidden;
    background: radial-gradient(ellipse at 55% 30%, var(--red-bright) 0%, var(--red) 50%, var(--red-deep) 100%);
  }
  .brand-name {
    position: absolute; left: 0; right: 0; top: 40px; text-align: center;
    font-family: "Russo One", sans-serif; font-size: 118px; line-height: 1; letter-spacing: 6px;
    color: var(--silver-light);
  }
  .product-line {
    position: absolute; left: 0; right: 0; top: 170px; text-align: center;
    font-family: "Open Sans", sans-serif; font-size: 27px; color: var(--black); letter-spacing: 0.5px;
  }
  .wave-bands { position: absolute; left: 0; top: 0; width: 500px; height: 560px; }
  .claim {
    position: absolute; right: 34px; top: 436px;
    font-family: "Open Sans", sans-serif; font-weight: 700; font-style: italic;
    font-size: 30px; color: var(--red-bright);
  }
  .contents {
    position: absolute; left: 40px; right: 20px; top: 488px;
    font-family: "Open Sans", sans-serif; font-weight: 700; font-style: italic;
    font-size: 21px; color: var(--white); white-space: nowrap;
  }
  .contents-count { font-size: 34px; margin-right: 6px; }
</style>
</head>
<body>
<main class="canvas">
  <section class="hanger-tab">
    <div class="hang-slot"></div>
    <div class="tab-brand">
      <span class="tab-brand-mark"></span>
      <span class="tab-brand-name">VOLK</span>
    </div>
    <p class="tab-tagline">WARM TIDE CONDOMS</p>
  </section>

  <section class="side-panel">
    <svg class="side-bands" viewBox="0 0 110 560" aria-hidden="true">
      <path d="M0 250 C40 300 80 330 110 340 L110 380 C70 360 30 330 0 300Z" fill="#9a9a9a"/>
      <path d="M0 300 C30 330 70 360 110 380 L110 420 C70 400 30 370 0 350Z" fill="#d80f0f"/>
      <path d="M0 350 C30 370 70 400 110 420 L110 455 C70 440 30 420 0 400Z" fill="#c9c9c9"/>
    </svg>
  </section>

  <section class="front-panel">
    <h1 class="brand-name">VOLK</h1>
    <p class="product-line">WARM TIDE CONDOMS</p>
    <svg class="wave-bands" viewBox="0 0 500 560" aria-hidden="true">
      <defs>
        <linearGradient id="silverBand" x1="0" y1="0" x2="1" y2="0">
          <stop offset="0" stop-color="#7d7d7d"/>
          <stop offset="0.5" stop-color="#c9c9c9"/>
          <stop offset="1" stop-color="#8f8f8f"/>
        </linearGradient>
      </defs>
      <path d="M0 355 C120 300 270 280 500 300 L500 560 L0 560Z" fill="url(#silverBand)"/>
      <path d="M0 385 C140 330 290 318 500 335 L500 560 L0 560Z" fill="#e9e9e9"/>
      <path d="M0 420 C140 355 300 345 500 360 L500 382 C300 372 150 392 0 452Z" fill="#d80f0f"/>
      <path d="M0 478 C150 408 310 398 500 412 L500 560 L0 560Z" fill="#111111"/>
    </svg>
    <p class="claim">For more pleasure</p>
    <p class="contents"><span class="contents-count">2</span>Individually tested latex condoms</p>
  </section>
</main>
</body>
</html>
```